Business card for our large format printing and installation business

We want a professional looking business card for our business. We manufacture and install Signs.

On the back of the card add this info
Large Format Graphics Printing & Installations, Event Graphics, Banners, Posters, Vehicle Fleet Graphics, Boat Wraps, Wall Murals, Decals,Displays,Signs,Plaques,Digital Signs

On the Front of the card add the Tallowfern Signs logo, plus On the back of the card add the Orange Tallowfern Wraps logo. The 2 vector logos are attached to the design brief.

Target Market(s)

Local business owners

Contact Information for Business Card

Colors
f37122
f68d4e
f9ba93

Requirements
Must have
• On the Front of the card add the Tallowfern Signs logo, plus On the back of the card add the Orange Tallowfern Wraps logo. The 2 vector logos are attached to the design brief.

```html
<!DOCTYPE html>
<html lang="en">
<head>
<meta charset="utf-8">
<title>Tallowfern Signs — Business Card</title>
<link href="https://fonts.googleapis.com/css2?family=Roboto+Condensed:wght@300;400;700&display=swap" rel="stylesheet">
<style>
  :root {
    --page: #3a3a3a;
    --card: #141414;
    --accent: #f37122;
    --accent-warm: #f9a43a;
    --ink: #f2f2f2;
    --muted: #cfcfcf;
  }
  * { box-sizing: border-box; margin: 0; padding: 0; }
  html, body { width: 1200px; height: 1021px; overflow: hidden; background: var(--page); }
  body {
    font-family: "Roboto Condensed", "Arial Narrow", sans-serif;
    position: relative;
  }
  .card {
    position: absolute;
    left: 180px;
    width: 840px;
    height: 480px;
    background: var(--card);
    box-shadow: 0 10px 30px rgba(0,0,0,.45);
    color: var(--ink);
  }
  .card--back { top: 20px; }
  .card--front { top: 521px; }

  .wordmark {
    position: absolute;
    font-weight: 700;
    color: var(--accent-warm);
    line-height: .95;
    letter-spacing: 1px;
  }
  .wordmark span { display: block; }

  /* back */
  .services {
    position: absolute;
    left: 70px;
    top: 110px;
  }
  .services__heading {
    color: var(--accent-warm);
    font-size: 25px;
    font-weight: 400;
    text-transform: uppercase;
    letter-spacing: .5px;
    line-height: 1.45;
  }
  .services__list {
    margin-top: 16px;
    list-style: none;
    font-size: 25px;
    font-weight: 300;
    line-height: 1.7;
    padding-left: 90px;
  }
  .services__list .dot { color: var(--accent); padding: 0 6px; }
  .card--back .wordmark { right: 60px; bottom: 60px; font-size: 64px; text-align: right; }

  /* front */
  .card--front .wordmark { left: 60px; top: 60px; font-size: 72px; }
  .contact {
    position: absolute;
    right: 70px;
    top: 150px;
    width: 420px;
  }
  .contact__name { color: var(--accent-warm); font-size: 28px; font-weight: 700; }
  .contact__title { font-size: 20px; font-weight: 300; color: var(--muted); margin-top: 2px; }
  .contact__rule { width: 48px; height: 3px; background: var(--accent); margin: 20px 0 18px; }
  .contact__lines { list-style: none; font-size: 23px; font-weight: 300; line-height: 1.3; }
  .contact__lines li { display: flex; align-items: center; gap: 10px; }
  .contact__lines svg { width: 18px; height: 18px; flex: none; }
  .contact__lines .no-icon { padding-left: 28px; }
</style>
</head>
<body>

<section class="card card--back" aria-label="Card back">
  <div class="services">
    <p class="services__heading">Large Format Graphics<br>Printing &amp; Installations</p>
    <ul class="services__list">
      <li>Banners<span class="dot">•</span>Posters</li>
      <li>Vehicle Graphics<span class="dot">•</span>Boat Wraps</li>
      <li>Wall Murals<span class="dot">•</span>Decals<span class="dot">•</span>Displays</li>
      <li>Signs<span class="dot">•</span>Plaques<span class="dot">•</span>Digital Signs</li>
    </ul>
  </div>
  <p class="wordmark"><span>Tallowfern</span><span>Wraps</span></p>
</section>

<section class="card card--front" aria-label="Card front">
  <p class="wordmark"><span>Tallowfern</span><span>Signs</span></p>
  <div class="contact">
    <p class="contact__name">Marcus Halloway</p>
    <p class="contact__title">CEO</p>
    <div class="contact__rule"></div>
    <ul class="contact__lines">
      <li class="no-icon">1840 Harbor View Lane #7</li>
      <li class="no-icon">Coral Bend, FL 33120</li>
      <li>
        <svg viewBox="0 0 24 24" fill="#f37122"><path d="M6.6 10.8a15.1 15.1 0 0 0 6.6 6.6l2.2-2.2a1 1 0 0 1 1-.25 11.4 11.4 0 0 0 3.6.57 1 1 0 0 1 1 1V20a1 1 0 0 1-1 1A17 17 0 0 1 3 4a1 1 0 0 1 1-1h3.5a1 1 0 0 1 1 1c0 1.25.2 2.45.57 3.57a1 1 0 0 1-.25 1z"/></svg>
        555-214-3870
      </li>
      <li>
        <svg viewBox="0 0 24 24" fill="#f37122"><path d="M6.6 10.8a15.1 15.1 0 0 0 6.6 6.6l2.2-2.2a1 1 0 0 1 1-.25 11.4 11.4 0 0 0 3.6.57 1 1 0 0 1 1 1V20a1 1 0 0 1-1 1A17 17 0 0 1 3 4a1 1 0 0 1 1-1h3.5a1 1 0 0 1 1 1c0 1.25.2 2.45.57 3.57a1 1 0 0 1-.25 1z"/></svg>
        555-608-4192 Direct
      </li>
      <li>
        <svg viewBox="0 0 24 24" fill="none" stroke="#f37122" stroke-width="2"><rect x="3" y="5" width="18" height="14"/><path d="M3 5l9 8 9-8"/></svg>
        marcus@tallowfern.net
      </li>
      <li>
        <svg viewBox="0 0 24 24" fill="none" stroke="#f37122" stroke-width="2"><circle cx="12" cy="12" r="9"/><path d="M3 12h18M12 3c3 3 3 15 0 18M12 3c-3 3-3 15 0 18"/></svg>
        www.tallowfernwraps.com
      </li>
    </ul>
  </div>
</section>

</body>
</html>
```